Stationery Design Project

I would like professional stationery that will be branded with our logo.

also, I have application- multipage that I would like to brand. I will attach an example of one of the pages.

Perhaps- this could be the same design, but due to spacing, it may be best to do slight variations.

Target Market(s)

The audience is our donors and supporters who have a heart for the disenfranchised. They are mostly professional and often have significant wealth. They do their work with excellence and I want an image that makes them feel confident we know what we are doing. this is why i tend to say i want a professional look. Also, I want the feel to be uplifting, something that is somewhat artistic and classy.

Industry/Entity Type

It Professional

Font styles to use
Serif

Requirements
Must have
• Generally, simple but I do want a stylized look...

583-274-6150
www.brightfernway.org
PO Box 384729 Dallas, TX 75211
admin@brightfernway.org
Nice to have
• i like to use the colors in our logo
Should not have
• hearts and country look

```html
<!DOCTYPE html>
<html lang="en">
<head>
<meta charset="utf-8">
<title>Bright Fern Way — Letterhead</title>
<link rel="stylesheet" href="https://fonts.googleapis.com/css2?family=Cinzel:wght@600&family=Oswald:wght@600&family=Source+Sans+3:wght@400&display=swap">
<style>
  :root{
    --backdrop:#e9e6e1;
    --paper-warm:#fffbd8;
    --paper-cool:#f1fbfc;
    --ink:#111111;
    --navy:#0b62b8;
    --sky:#0aa3ee;
    --sun:#ffd400;
    --icon-soft:#f8e27a;
    --seal-white:#ffffff;
    --ghost:#c3c8c3;
  }
  html,body{margin:0;padding:0;width:900px;height:1200px;overflow:hidden;background:var(--backdrop);}
  .canvas{position:relative;width:900px;height:1200px;}
  .letterhead{
    position:absolute;left:22px;top:52px;width:850px;height:1100px;overflow:hidden;
    background:linear-gradient(90deg,var(--paper-warm) 0%,var(--paper-cool) 100%);
  }
  .brand-seal{
    position:absolute;left:332px;top:17px;width:186px;height:186px;border-radius:50%;
    background:var(--seal-white);display:flex;flex-direction:column;align-items:center;justify-content:center;
  }
  .brand-seal__mark{width:58px;height:58px;border-radius:50%;background:var(--sky);margin-bottom:12px;}
  .brand-seal__name{
    font-family:"Cinzel",serif;font-weight:600;color:var(--ink);font-size:19px;line-height:1.1;text-align:center;letter-spacing:.5px;
  }
  .ghost-name{
    position:absolute;left:600px;top:930px;width:210px;text-align:center;
    font-family:"Cinzel",serif;font-weight:600;color:var(--ghost);font-size:40px;line-height:1.1;
  }
  .footer-bands{position:absolute;left:0;top:0;width:850px;height:1100px;}
  .footer-info{
    position:absolute;left:74px;top:1068px;height:20px;display:flex;align-items:center;
    font-family:"Source Sans 3",sans-serif;font-size:15px;color:var(--ink);white-space:nowrap;
  }
  .footer-info__name{font-family:"Oswald",sans-serif;font-weight:600;font-size:14px;letter-spacing:.2px;margin-right:22px;}
  .footer-info__item{display:flex;align-items:center;margin-right:12px;}
  .footer-info__item svg{width:12px;height:14px;margin-right:5px;fill:var(--icon-soft);}
</style>
</head>
<body>
<div class="canvas">
  <main class="letterhead">
    <div class="brand-seal">
      <span class="brand-seal__mark"></span>
      <div class="brand-seal__name">Bright<br>Fern Way</div>
    </div>

    <div class="ghost-name" aria-hidden="true">Bright<br>Fern Way</div>

    <svg class="footer-bands" viewBox="0 0 850 1100" aria-hidden="true">
      <polygon fill="var(--navy)" points="0,1045 425,1018 850,1043 850,1100 0,1100"/>
      <polygon fill="var(--sky)" points="0,1053 425,1028 850,1052 850,1100 0,1100"/>
      <polygon fill="var(--sun)" points="0,1066 425,1038 850,1066 850,1100 0,1100"/>
    </svg>

    <footer class="footer-info">
      <span class="footer-info__name">BRIGHT FERN WAY</span>
      <span class="footer-info__item">
        <svg viewBox="0 0 12 14"><path d="M6 0a5 5 0 0 0-5 5c0 3.6 5 9 5 9s5-5.4 5-9a5 5 0 0 0-5-5zm0 7a2 2 0 1 1 0-4 2 2 0 0 1 0 4z"/></svg>
        PO Box 384729&nbsp; Dallas,&nbsp; TX 75211
      </span>
      <span class="footer-info__item">
        <svg viewBox="0 0 12 14"><path d="M2.5 1l2 .3 1 3-1.4 1.2a7 7 0 0 0 3.4 3.6l1.2-1.4 3 1-.2 2.2c-.1.8-.8 1.3-1.6 1.2C4.6 11.5 1 7.6.8 2.6.8 1.7 1.6 1 2.5 1z"/></svg>
        583-274-6150
      </span>
      <span class="footer-info__item">
        <svg viewBox="0 0 14 14" style="width:14px"><path d="M1 3h12v8H1z M1 3l6 4.5L13 3" fill="none" stroke="var(--icon-soft)" stroke-width="1.4"/></svg>
        admin@brightfernway.org
      </span>
    </footer>
  </main>
</div>
</body>
</html>
```